Local Newspaper Quarterly " Meet The Realtor" print ad

I need a new add made up. This was my last ad:
http://www.heraldpostlistings.example/static/pdfs/agents1309/Ar092213%20G10%20006%20Prepress.pdf

I do not really care of Realtor advertisements because they are just so cheesy and rather pompous-like. However, it's a necessary evil
My ads have always been outside of the box and/or visually sharp.
I now have a new company' Vorel Real Estate( I will attach a logo) contact info:
Cale Vorel
Vorel Real Estate
Broker/Owner( this can be somewhere in small print or corner of ad since it's mandatory to have shown
Phone: 304-555-0147
Email: Cale@VorelRealEstate.Example
VorelRealEstate.Example
I would like social icons(FB,Twitter, Pinterest! Houzz, Gplus)

Ideas: In my logo font or using the image at the top I envision
Something like:
A
Vorel Real Estate
Of Mind
Body of ad?
Images of Charleston WV as a real light back ground
With 3 or 4 customer reviews chosen by you in this site:
http://webcale.example/think.html

Bottom: contact info and my name in a nice Signature style ??
My agent pic at the bottom right( to be small. I don't want my big head overshadowing the message)

I have yet to think of a tagline for my new company:
I have been thinking of " Luxury Services For All Things Real Estate"

Or nothing at all ??? I don't care for tag lines but then again that's part of the business

Target Market(s)

Higher end homes

Industry/Entity Type

Business

Colors
0f59a5
0392cd
0f0f0f
eaeaea
ffffff

Requirements
Must have
• My logo and colors
Nice to have
• My agent picture and client review.
Should not have
• No typical real estate images like a house or home buyer

```html
<!DOCTYPE html>
<html lang="en">
<head>
<meta charset="utf-8">
<title>Vorel Real Estate – Luxury Services For All Things Real Estate</title>
<link rel="stylesheet" href="https://fonts.googleapis.com/css2?family=Jost:ital,wght@0,300;0,400;0,500;0,700;1,400;1,500&display=swap">
<style>
  :root {
    --brand-blue: #1b74ba;
    --band-dark: #3e3e3e;
    --white: #ffffff;
    --light: #eaeaea;
    --ink: #0f0f0f;
    --sky-top: #c9d6e2;
    --city-mid: #8a8378;
    --river: #5d7a58;
  }
  html, body {
    margin: 0;
    padding: 0;
    width: 769px;
    height: 1200px;
    overflow: hidden;
    background: var(--white);
  }
  .ad {
    position: relative;
    width: 769px;
    height: 1200px;
    overflow: hidden;
    background: var(--white);
    font-family: "Jost", "Futura", sans-serif;
    color: var(--white);
  }
  .hero-photo {
    position: absolute;
    left: 0;
    top: 123px;
    width: 769px;
    height: 480px;
    background: linear-gradient(180deg,
      var(--sky-top) 0%,
      #dfe4e8 18%,
      #8e8a80 30%,
      #a07a63 45%,
      var(--city-mid) 55%,
      #6f8b6a 63%,
      var(--river) 78%,
      #7a6a5a 100%);
  }
  .blue-field {
    position: absolute;
    left: 0;
    top: 603px;
    width: 769px;
    height: 597px;
    background: var(--brand-blue);
  }
  .headline {
    position: absolute;
    left: 34px;
    top: 538px;
    margin: 0;
    font-weight: 300;
    font-size: 84px;
    line-height: 1;
    letter-spacing: -1px;
    color: var(--white);
  }
  .subhead {
    position: absolute;
    left: 138px;
    top: 630px;
    margin: 0;
    display: flex;
    align-items: flex-end;
    gap: 14px;
    font-weight: 400;
  }
  .subhead-small {
    font-weight: 300;
    font-size: 32px;
    line-height: 37px;
    text-align: right;
  }
  .subhead-large {
    font-weight: 400;
    font-size: 110px;
    line-height: 96px;
    letter-spacing: -1.5px;
  }
  .logo-box {
    position: absolute;
    left: 37px;
    top: 838px;
    width: 102px;
    height: 102px;
    border: 3px solid var(--white);
    background: linear-gradient(135deg, #9a9a9a 0%, #4b4b4b 100%);
    display: flex;
    flex-direction: column;
    align-items: center;
    justify-content: center;
    gap: 6px;
  }
  .logo-mark {
    width: 14px;
    height: 14px;
    border-radius: 50%;
    background: var(--white);
  }
  .logo-name {
    font-weight: 500;
    font-size: 14px;
    line-height: 17px;
    text-align: center;
    letter-spacing: 1px;
    color: var(--white);
    text-transform: uppercase;
  }
  .reviews {
    position: absolute;
    left: 261px;
    top: 767px;
    width: 472px;
    font-weight: 300;
    font-size: 11.7px;
    line-height: 16.3px;
    text-align: justify;
  }
  .reviews p { margin: 0 0 16.3px; }
  .reviews .intro { margin-bottom: 16.3px; }
  .review-author { font-style: italic; font-weight: 400; }
  .call-to-action { font-weight: 400; }
  .contact-band {
    position: absolute;
    left: 0;
    top: 1067px;
    width: 769px;
    height: 84px;
    background: var(--band-dark);
  }
  .agent-photo {
    position: absolute;
    left: 37px;
    top: 1055px;
    width: 102px;
    height: 102px;
    border: 3px solid var(--white);
    background: linear-gradient(160deg, #c58a3a 0%, #a8b4bd 55%, #dfe3e6 100%);
  }
  .contact {
    position: absolute;
    left: 158px;
    top: 1079px;
    font-size: 11px;
    line-height: 15px;
    font-weight: 300;
    color: var(--light);
  }
  .contact-name {
    font-weight: 700;
    font-size: 14px;
    letter-spacing: 0.5px;
    color: var(--white);
    margin-bottom: 3px;
  }
  .social {
    position: absolute;
    left: 536px;
    top: 1103px;
    display: flex;
    gap: 7px;
  }
  .social-link {
    width: 27px;
    height: 26px;
    background: var(--white);
    display: block;
  }
</style>
</head>
<body>
<main class="ad">
  <div class="hero-photo" role="img" aria-label="Photograph of a city skyline across the river with a steel truss bridge"></div>
  <div class="blue-field"></div>

  <h1 class="headline">Luxury Services</h1>
  <div class="subhead">
    <span class="subhead-small">For All<br>Things</span>
    <span class="subhead-large">Real Estate</span>
  </div>

  <div class="logo-box" aria-label="Vorel Real Estate">
    <span class="logo-mark"></span>
    <span class="logo-name">Vorel<br>Real Estate</span>
  </div>

  <section class="reviews">
    <p class="intro">See what the people are saying…</p>
    <p>In trying to buy a home from long distance, Cale went above and beyond his duty as my Realtor. His professionalism, knowledge and attentiveness were absolutely superb! What could have been a nightmare experience, turned out to be a wonderfully smooth transition. Thanks for all your help – it was truly appreciated! A++ <span class="review-author">~ Dana Whitlow</span></p>
    <p>In this difficult sales market, I believe every effort was made to sell our home successfully. We truly appreciate the expenditure of time , energy and resources by Vorel Real Estate and their encouragement and persistence extended in this successful outcome. <span class="review-author">~ Owen and Lisa Harrold</span></p>
    <p>We have and will recommend Cale Vorel to anyone looking to buy or sell any Real Estate. We feel Cale did an exceptional job selling our property even that it was was at the low end of the Real Estate market. <span class="review-author">~ Mark and Erin Tolliver</span></p>
    <p class="call-to-action">Call me today to book an appointment.</p>
  </section>

  <div class="contact-band"></div>
  <div class="agent-photo" role="img" aria-label="Portrait photo of agent Cale Vorel outdoors"></div>
  <div class="contact">
    <div class="contact-name">Cale Vorel - For more information call 304-555-0147</div>
    <div>Broker/Owner • Vorel Real Estate</div>
    <div>Cale@VorelRealEstate.Example</div>
    <div>Visit VorelRealEstate.Example today.</div>
  </div>
  <nav class="social" aria-label="Social profiles">
    <span class="social-link" aria-label="Social profile 1"></span>
    <span class="social-link" aria-label="Social profile 2"></span>
    <span class="social-link" aria-label="Social profile 3"></span>
    <span class="social-link" aria-label="Social profile 4"></span>
    <span class="social-link" aria-label="Social profile 5"></span>
    <span class="social-link" aria-label="Social profile 6"></span>
  </nav>
</main>
</body>
</html>
```